Personal Blog

The wordpress blog style and layout should be similar to http://www.ninalofwent.com

homepage: my photo, list of things, call to action then 3 boxes (The Blog, The Book and podcast)

Other pages: About us, Blog, Consulting, Contact

Target Market(s)

Web Marketing Consultant

Industry/Entity Type

Consulting

Colors
3277b5
33a6d7
f04a50
f68e4e
33b7a4

```html
<!DOCTYPE html>
<html lang="en">
<head>
<meta charset="utf-8">
<title>Business Bootcamp – Personal Blog</title>
<link href="https://fonts.googleapis.com/css2?family=Cabin:wght@400;500;600;700&family=Arimo:wght@400;700&display=swap" rel="stylesheet">
<style>
  :root {
    --teal: #33b7a4;
    --blue: #33a6d7;
    --navy: #3277b5;
    --red: #f04a50;
    --orange: #f68e4e;
    --page: #ebebeb;
    --white: #ffffff;
    --ink: #555555;
    --soft-ink: #777777;
    --tick: #2e9e3e;
    --partner: #8a8a8a;
  }
  * { margin: 0; padding: 0; box-sizing: border-box; }
  html, body { width: 1200px; height: 1000px; overflow: hidden; }
  body {
    position: relative;
    background: var(--page);
    font-family: "Arimo", Arial, sans-serif;
    color: var(--ink);
  }
  .abs { position: absolute; }

  /* Header */
  .site-header {
    position: absolute; left: 0; top: 0; width: 1200px; height: 63px;
    background: var(--teal);
    border-bottom: 3px solid var(--white);
  }
  .logo-text {
    position: absolute; left: 277px; top: 18px;
    font: 700 18px/22px "Arimo", Arial, sans-serif; color: var(--white);
    letter-spacing: 0.2px;
  }
  .main-nav a {
    position: absolute; top: 23px;
    font: 700 10px/12px "Arimo", Arial, sans-serif; color: var(--white);
    text-decoration: none;
  }

  /* Hero */
  .hero-photo {
    left: 277px; top: 108px; width: 174px; height: 254px;
    background: linear-gradient(180deg, #d9d9d9 0%, #9a9a9a 40%, #5d5f62 100%);
    border-radius: 70px 70px 0 0;
  }
  .hero-title {
    left: 503px; top: 115px; white-space: nowrap;
    font: 700 20.6px/24px "Arimo", Arial, sans-serif; color: var(--ink);
  }
  .hero-title .accent { color: var(--teal); }
  .hero-sub {
    left: 505px; top: 144px; white-space: nowrap;
    font: 700 11.6px/15px "Arimo", Arial, sans-serif; color: var(--ink);
  }
  .hero-list { left: 507px; top: 176px; list-style: none; }
  .hero-list li {
    display: flex; align-items: center; gap: 7px;
    height: 18.2px; white-space: nowrap;
    font: 400 9.5px/12px "Arimo", Arial, sans-serif; color: var(--ink);
  }
  .hero-list svg { width: 12px; height: 10px; flex: none; }

  .cta-button {
    display: flex; align-items: center; justify-content: center;
    background: var(--red); color: var(--white);
    font: 600 13px/1 "Cabin", Arial, sans-serif;
    text-decoration: none;
  }
  .hero-cta { left: 508px; top: 294px; width: 110px; height: 32px; }

  /* Featured strip */
  .featured-strip {
    left: 277px; top: 362px; width: 645px; height: 43px;
    background: var(--white);
    box-shadow: 0 -3px 6px rgba(0,0,0,0.12);
  }
  .featured-label {
    position: absolute; left: 12px; top: 15px;
    font: 500 11.5px/13px "Cabin", Arial, sans-serif; color: var(--ink);
    letter-spacing: 0.6px;
  }
  .partner-name {
    position: absolute; top: 15px; white-space: nowrap;
    font: 700 12px/13px "Cabin", Arial, sans-serif; color: var(--partner);
  }

  .intro-text {
    left: 300px; top: 419px; width: 600px; text-align: center;
    font: 700 12.5px/20px "Cabin", Arial, sans-serif; color: var(--soft-ink);
  }
  .intro-text .source { color: #999; }

  /* Feature boxes */
  .feature-box {
    top: 475px; width: 205px; height: 212px; background: var(--white);
  }
  .feature-box .box-head {
    height: 39px; display: flex; align-items: center; justify-content: center;
    font: 600 14.5px/1 "Cabin", Arial, sans-serif; color: var(--white);
    text-transform: uppercase; padding-top: 2px;
  }
  .box-blog .box-head { background: var(--blue); }
  .box-book .box-head { background: var(--orange); }
  .box-podcast .box-head { background: var(--teal); }
  .feature-box p {
    position: absolute; left: 16px; top: 51px; width: 180px;
    font: 400 9px/15.5px "Arimo", Arial, sans-serif; color: var(--soft-ink);
  }
  .feature-box .read-more {
    position: absolute; left: 16px; top: 121px;
    font: 400 8px/10px "Arimo", Arial, sans-serif; text-decoration: underline;
  }
  .box-blog .read-more { color: var(--blue); }
  .box-book .read-more { color: var(--orange); }
  .box-podcast .read-more { color: var(--teal); }
  .feature-box .box-image {
    position: absolute; left: 14px; top: 142px; width: 176px; height: 57px;
  }
  .box-blog .box-image { background: linear-gradient(90deg, #3a2a30, #8a5a50 55%, #c9a07a); }
  .box-book .box-image { background: linear-gradient(90deg, #d8d2c8, #8c8478 60%, #5a5048); }
  .box-podcast .box-image { background: linear-gradient(90deg, #b08a60, #e6dcd0 50%, #6a4a3a); }

  /* Book panel */
  .book-panel {
    left: 277px; top: 704px; width: 645px; height: 207px; background: var(--white);
  }
  .book-panel h2 {
    position: absolute; left: 17px; top: 25px;
    font: 600 15px/18px "Cabin", Arial, sans-serif; color: var(--ink);
  }
  .book-cover {
    position: absolute; left: 18px; top: 60px; width: 166px; height: 122px;
    background: linear-gradient(100deg, #3c8ac4 0%, #e9c27a 55%, #2f6fb0 100%);
    border-radius: 2px;
  }
  .book-panel p {
    position: absolute; left: 227px; top: 58px; width: 400px;
    font: 400 11.6px/15.5px "Cabin", Arial, sans-serif; color: var(--soft-ink);
  }
  .book-cta { left: 227px; top: 147px; width: 101px; height: 32px; }

  /* Footer */
  .site-footer {
    position: absolute; left: 0; top: 927px; width: 1200px; height: 73px;
    background: var(--teal); color: var(--white); text-align: center;
    font: 400 8.5px/12px "Cabin", Arial, sans-serif;
    padding-top: 23px;
  }
  .site-footer a { color: var(--white); text-decoration: none; }
</style>
</head>
<body>

<header class="site-header">
  <div class="logo-text">YOUR LOGO</div>
  <nav class="main-nav">
    <a href="#" style="left:635px">Home</a>
    <a href="#" style="left:690px">About Us</a>
    <a href="#" style="left:756px">Blog</a>
    <a href="#" style="left:812px">Consulting</a>
    <a href="#" style="left:888px">Contact</a>
  </nav>
</header>

<section class="hero">
  <div class="hero-photo abs" role="img" aria-label="Portrait photo of the consultant in a grey suit, arms crossed"></div>
  <h1 class="hero-title abs">Join My New Business <span class="accent">Bootcamp</span> for Free!</h1>
  <div class="hero-sub abs">Lorem Ipsum is simply dummy text of the printing and typesetting industry.</div>
  <ul class="hero-list abs">
    <li><svg viewBox="0 0 12 10"><path d="M1 5.5 L4.5 9 L11 1.5" fill="none" stroke="#2e9e3e" stroke-width="2.6"/></svg>Lorem Ipsum is simply dummy text of the printing and typesetting</li>
    <li><svg viewBox="0 0 12 10"><path d="M1 5.5 L4.5 9 L11 1.5" fill="none" stroke="#2e9e3e" stroke-width="2.6"/></svg>Lorem Ipsum is simply dummy text</li>
    <li><svg viewBox="0 0 12 10"><path d="M1 5.5 L4.5 9 L11 1.5" fill="none" stroke="#2e9e3e" stroke-width="2.6"/></svg>Lorem Ipsum is simply dummy text of the printing</li>
    <li><svg viewBox="0 0 12 10"><path d="M1 5.5 L4.5 9 L11 1.5" fill="none" stroke="#2e9e3e" stroke-width="2.6"/></svg>Lorem Ipsum is simply dummy text of the printing&nbsp; typesetting</li>
    <li><svg viewBox="0 0 12 10"><path d="M1 5.5 L4.5 9 L11 1.5" fill="none" stroke="#2e9e3e" stroke-width="2.6"/></svg>Lorem Ipsum is simply dummy text&nbsp; and typesetting</li>
  </ul>
  <a href="#" class="cta-button hero-cta abs">Call to Action</a>
</section>

<section class="featured-strip abs">
  <span class="featured-label">AS FEATURED IN</span>
  <span class="partner-name" style="left:138px">Harvlo</span>
  <span class="partner-name" style="left:199px">Zumin</span>
  <span class="partner-name" style="left:262px">Quellan</span>
  <span class="partner-name" style="left:332px">Tovaplex</span>
  <span class="partner-name" style="left:407px">Ebrynt</span>
  <span class="partner-name" style="left:482px">Wulvaro</span>
  <span class="partner-name" style="left:553px">Sorquin</span>
</section>

<p class="intro-text abs">Lorem Ipsum is simply dummy text of the printing and typesetting industry. Lorem Ipsum has been the industry's standard - <span class="source">Lorem Ipsum</span></p>

<article class="feature-box box-blog abs" style="left:277px">
  <div class="box-head">The Blog</div>
  <p>Lorem Ipsum is simply dummy text of the printing and typesetting industry. Lorem Ipsum has been the industry's standard dummy text ever since</p>
  <a href="#" class="read-more">READ MORE</a>
  <div class="box-image" role="img" aria-label="Photo of a couple wearing sunglasses"></div>
</article>

<article class="feature-box box-book abs" style="left:498px">
  <div class="box-head">The Book</div>
  <p>Lorem Ipsum is simply dummy text of the printing and typesetting industry. Lorem Ipsum has been the industry's standard dummy text ever since</p>
  <a href="#" class="read-more">READ MORE</a>
  <div class="box-image" role="img" aria-label="Photo of brushes resting on an open book"></div>
</article>

<article class="feature-box box-podcast abs" style="left:718px">
  <div class="box-head">The Podcast</div>
  <p>Lorem Ipsum is simply dummy text of the printing and typesetting industry. Lorem Ipsum has been the industry's standard dummy text ever since</p>
  <a href="#" class="read-more">READ MORE</a>
  <div class="box-image" role="img" aria-label="Photo of a woman listening with headphones"></div>
</article>

<section class="book-panel abs">
  <h2>Lorem Ipsum is simply dummy text of the printing</h2>
  <div class="book-cover" role="img" aria-label="Two copies of the book shown standing at an angle"></div>
  <p>Lorem Ipsum is simply dummy text of the printing and typesetting industry. Lorem Ipsum has been the industry's standard dummy text ever since the 1500s, when an unknown printer took a galley of type and scrambled it to make a type specimen book.</p>
  <a href="#" class="cta-button book-cta abs">Call to Action</a>
</section>

<footer class="site-footer">
  <div><a href="#">Friendbook</a> &nbsp;|&nbsp; <a href="#">Chirper</a> &nbsp;|&nbsp; <a href="#">WorkLinks</a></div>
  <div>Copyright © 2014 Company Name</div>
</footer>

</body>
</html>
```